The Corvane Agency

We are a pr, social media and strategy agency specializing in the pet industry. We would like a new dynamic design of our existing website. We think it is currently outdated and looks too corporate. We would like it to look more consumer oriented as we primarily market pet products. We would like warm imagery involving pets and while pets are fun, this is still a business website and needs to maintain a professional look. We are hired by business owners and executives.
I would like some of our work featured on the home page.
Our primary service tabs are:
Public Relations
Social Media
Product Consulting
Most of the content will remain the same but we are open to suggestions!
Our current website can be found at www.corvanepetpr.example.
We are open to other colors than in our logo and on our current page.
This is a design only project and will not require programming. The selected designer will need to provide at least one interior page in addition to the home page.

Industry/Entity Type

Pet

Requirements
Should not have
• Cartoon type figures. Pet puns.

```html
<!DOCTYPE html>
<html lang="en">
<head>
<meta charset="utf-8">
<title>The Corvane Agency</title>
<link href="https://fonts.googleapis.com/css2?family=Raleway:wght@200;300&family=Open+Sans:wght@400;600;700&family=Roboto+Condensed:wght@300;400&family=Oswald:wght@500;700&family=Noto+Serif:ital@1&display=swap" rel="stylesheet">
<style>
:root{
  --night:#2f3237;
  --mist:#ececee;
  --paper:#ffffff;
  --wine:#8c1a1d;
  --red:#b8191e;
  --brand:#d3262c;
  --amber:#f7a51c;
  --peach:#e9a98a;
  --teal:#1c8a9a;
  --leaf:#6fbf4e;
  --ink:#4a4a4a;
  --link:#2a6bb0;
  --coral:#f08a73;
}
*{margin:0;padding:0;box-sizing:border-box}
html,body{width:768px;height:1200px;overflow:hidden}
body{position:relative;background:var(--mist);font-family:"Open Sans",sans-serif;color:var(--ink)}
a{color:inherit;text-decoration:none}
.backdrop-top{position:absolute;left:0;top:0;width:768px;height:332px;background:var(--night)}
.page{position:absolute;left:95px;top:24px;width:580px;height:1000px;background:var(--paper);box-shadow:0 0 6px rgba(0,0,0,.25)}
.page-cap{position:absolute;left:95px;top:18px}
.backdrop-foot{position:absolute;left:0;top:940px;width:768px;height:260px}
.logo{position:absolute;left:110px;top:46px;display:flex;align-items:center;gap:5px}
.logo-dot{width:7px;height:7px;border-radius:50%;background:var(--brand)}
.logo-name{font-weight:600;font-size:13px;color:var(--brand);line-height:1.05;width:84px}
.call{position:absolute;right:108px;top:50px;display:flex;gap:6px;align-items:flex-start}
.call-label{font-family:"Roboto Condensed",sans-serif;font-size:8.5px;color:#333;letter-spacing:.1px}
.call-number{font-family:"Oswald",sans-serif;font-weight:700;font-size:19px;color:var(--amber);line-height:1.05}
.nav-main{position:absolute;left:95px;top:97px;width:578px;height:25px;background:var(--wine);display:flex;justify-content:space-between;align-items:center;padding:0 12px 0 8px;font-weight:700;font-size:8px;color:#fff;text-transform:uppercase;letter-spacing:.3px}
.nav-main a{line-height:25px}
.nav-main a.current{background:var(--red);padding:0 12px}
.nav-sub{position:absolute;left:95px;top:122px;width:578px;height:23px;background:var(--red);display:flex;justify-content:center;align-items:center;font-size:7.6px;color:#fff;text-transform:uppercase;letter-spacing:.2px}
.nav-sub span.sep{margin:0 10px;opacity:.7}
.hero{position:absolute;left:96px;top:145px;width:576px;height:243px;background:linear-gradient(100deg,#7c6f66 0%,#d9b48a 25%,#8f8a82 50%,#c8b7a2 75%,#ece6de 100%)}
.hero-caption{position:absolute;left:96px;top:272px;width:340px;height:48px;background:rgba(233,169,138,.9);font-family:"Roboto Condensed",sans-serif;font-weight:300;font-size:27px;color:#fff;padding:6px 14px;letter-spacing:-.5px}
.hero-dots{position:absolute;left:600px;top:303px;display:flex;gap:4px}
.hero-dots i{width:6px;height:6px;border-radius:50%;background:#111}
.hero-dots i.on{background:var(--red)}
.hero-band{position:absolute;left:96px;top:320px;width:576px;height:68px;background:rgba(255,255,255,.72);padding:13px 12px;font-family:"Roboto Condensed",sans-serif;font-size:9.3px;color:#111;line-height:1.4}
.btn-more{position:absolute;left:606px;top:362px;width:54px;height:14px;border-radius:3px;background:linear-gradient(#2aa4b3,var(--teal));color:#fff;font-size:6.5px;line-height:14px;text-align:center}
.hero-shade{position:absolute;left:110px;top:388px;width:550px;height:14px;background:radial-gradient(ellipse at top,rgba(0,0,0,.55),transparent 70%)}
.story{position:absolute;left:105px;width:395px}
.story h2{font-family:"Raleway",sans-serif;font-weight:200;font-size:29px;color:#222;letter-spacing:-.3px;margin-bottom:12px}
.story h2 em{font-style:normal;color:var(--red)}
.story p{font-size:7.7px;line-height:1.55;margin-bottom:11px}
.btn-orange{display:inline-block;width:65px;height:16px;border-radius:8px;background:linear-gradient(#ffbf3a,#f28a10);color:#fff;font-size:6.5px;text-align:center;line-height:16px;text-transform:uppercase;box-shadow:0 1px 2px rgba(0,0,0,.3)}
.quote{position:absolute;left:537px;top:422px;width:126px;height:210px;background:var(--leaf);border-radius:10px 0 0 0;padding:10px 14px 10px 11px;color:#fff}
.quote h3{font-size:11px;font-weight:700;margin-bottom:6px}
.quote p{font-family:"Noto Serif",serif;font-style:italic;font-size:7.4px;line-height:1.42}
.quote-dots{display:flex;gap:4px;justify-content:center;margin-top:11px}
.quote-dots i{width:5px;height:5px;border-radius:50%;background:#e2f1da}
.quote-dots i.on{background:#b6dd9e}
.quote-tail{position:absolute;left:551px;top:631px}
.quote-author{position:absolute;left:541px;top:647px;font-family:"Noto Serif",serif;font-style:italic;font-size:7.2px;line-height:1.6;color:#777;padding-left:16px}
.quote-author b{font-weight:400;color:var(--leaf)}
.blog{position:absolute;left:537px;top:705px;width:126px;border:1px solid #ddd;background:#fff}
.blog h3{background:var(--red);color:#fff;font-size:10px;font-weight:700;padding:7px 11px;border-radius:8px 0 0 0;margin:-1px -1px 0}
.blog li{list-style:none;padding:6px 11px;border-top:1px solid #e2e2e2;font-size:7.3px;line-height:1.45}
.blog li:first-of-type{border-top:0}
.blog time{display:block;font-size:6.5px;color:#444}
.blog a{color:var(--link)}
.pets{position:absolute;left:258px;top:900px;width:232px;height:134px;background:linear-gradient(90deg,#d08a4a,#c7844e 30%,#e8ddd0 50%,#7a5038 65%,#d79a5f);border-radius:40px 40px 12px 12px;opacity:.9}
.pets-shadow{position:absolute;left:210px;top:1020px;width:350px;height:18px;background:radial-gradient(ellipse,rgba(0,0,0,.55),transparent 70%)}
.foot-links{position:absolute;left:0;width:768px;text-align:center;font-size:7px;color:#fff}
.foot-links span{margin:0 3px;opacity:.8}
.foot-note{position:absolute;top:1108px;width:768px;text-align:center;font-size:7px;color:var(--coral)}
.social{position:absolute;top:1141px;left:344px;display:flex;gap:6px}
.social i{width:22px;height:22px;border-radius:50%;background:#6b6e73}
</style>
</head>
<body>
<div class="backdrop-top"></div>

<div class="page"></div>
<svg class="page-cap" width="580" height="30" viewBox="0 0 580 30" aria-hidden="true">
  <path d="M0 30 V20 Q0 14 8 14 Q290 2 572 14 Q580 14 580 20 V30 Z" fill="#fff"/>
</svg>

<svg class="backdrop-foot" width="768" height="260" viewBox="0 0 768 260" aria-hidden="true">
  <path d="M0 52 Q384 -10 768 52 V260 H0 Z" fill="#2f3237"/>
</svg>

<header>
  <div class="logo"><span class="logo-dot"></span><span class="logo-name">The Corvane Agency</span></div>
  <div class="call">
    <svg width="10" height="26" viewBox="0 0 10 26" aria-hidden="true"><path d="M7 1 H3 Q1 1 1 4 V22 Q1 25 3 25 H7 V20 H4 V6 H7 Z" fill="#222"/></svg>
    <div>
      <div class="call-label">WE LOOK FORWARD TO HEARING FROM YOU!</div>
      <div class="call-number">555.014.2270</div>
    </div>
  </div>
  <nav class="nav-main">
    <a class="current">About Corvane</a><a>PR</a><a>Social Media</a><a>Pet Experts</a><a>Business Development</a><a>Case Studies</a><a>Our Team</a>
  </nav>
  <nav class="nav-sub">
    <a>Corvane Life</a><span class="sep">|</span><a>Connect With Us</a><span class="sep">|</span><a>Our Blog</a><span class="sep">|</span><a>Corporate Site</a><span class="sep">|</span><a>Contact</a><span class="sep">|</span><a>Careers</a><span class="sep">|</span><a>Love List</a><span class="sep">|</span><a>Blog</a>
  </nav>
</header>

<section>
  <div class="hero" role="img" aria-label="Photo of a litter of kittens held in a person's hands"></div>
  <div class="hero-caption">Redefining Pet Associations</div>
  <div class="hero-dots"><i></i><i></i><i class="on"></i><i></i><i></i></div>
  <div class="hero-band">The power of any association is the strength of its unity. We have managed a wide range of pet-related associations and tradeshows, brings teams together to deliver outstanding results.</div>
  <a class="btn-more">Read more &raquo;</a>
  <div class="hero-shade"></div>
</section>

<main>
  <article class="story" style="top:414px">
    <h2>Actions define <em>us</em></h2>
    <p>The word "corvane" has great meaning to us. It's the force that makes things happen, the motivation that turns nothing into something. For us, that stimulus is generated by a corporate culture that allows work to flow freely, projects to progress quickly, and ideas to flourish naturally.</p>
    <p>There really was no other name in the world that was a better fit. Our name carries "pet" and "us" in spirit, two words that together define who we are. We specialize in the pet industry through a team effort built on passionate individuals who understand the unique aspects of the multi-billion dollar pet industry.</p>
    <p>It's not a culture you'll find just anywhere. Achieving that perfect balance of public relations leadership skills, in-the-trenches attitude, team chemistry, and unified vision is something The Corvane Agency has worked diligently to hone.</p>
    <p>All that hard work translates into success for our clients. We tap the best ways to connect you with your audience, using modern marketing platforms and a full arsenal of social media outlets to speak to your audience on a level that is more specific, more engaging, and most of all, more personable.</p>
    <a class="btn-orange">Read more</a>
  </article>

  <article class="story" style="top:704px">
    <h2>Our <em>team</em></h2>
    <p>The driving force behind our success is the team that makes it happen. Individual skills and experience meet a collective desire to excel in every facet of our work and shape our daily approach to elevate the pet industry through our clients.</p>
    <p>Each member of our pack provides the strength and stability to run smoothly, yet it's our unified vision to always stay hungry, curious and happy that truly gives us a competitive edge.</p>
    <a class="btn-orange">Read more</a>
  </article>

  <aside>
    <div class="quote">
      <h3>&ldquo; Testimonials</h3>
      <p>The Corvane Agency has been a huge asset to us from the beginning. In the initial launch of Pawlane, they opened tremendous channels to numerous media outlets. They continued to provide industry exposure with skilled and experience social media guidance. Traditional media would have been costly, Corvane has been a great ROI for us.</p>
      <div class="quote-dots"><i class="on"></i><i></i><i></i><i></i></div>
    </div>
    <svg class="quote-tail" width="14" height="10" viewBox="0 0 14 10" aria-hidden="true"><path d="M0 0 H14 L0 10 Z" fill="#6fbf4e"/></svg>
    <div class="quote-author">
      <svg style="position:absolute;left:0;top:2px" width="10" height="10" viewBox="0 0 10 10" aria-hidden="true"><circle cx="5" cy="3" r="2.5" fill="#999"/><path d="M0 10 Q5 3 10 10 Z" fill="#999"/></svg>
      <b>Warren Ellery, MD</b><br>Pawlane, Inc.<br>Hope that helps! Warren
    </div>

    <div class="blog">
      <h3>Recent blog posts</h3>
      <ul>
        <li><time>03/01/2014</time><a>Trailbound Featured on Morning Tails</a></li>
        <li><time>07/10/2014</time><a>The Power of Stress</a></li>
        <li><time>13/08/2013</time><a>The Evolution of the Ideas: Brainstorming</a></li>
        <li><time>27/04/2012</time><a>Relationship Building</a></li>
      </ul>
    </div>
  </aside>
</main>

<footer>
  <div class="pets-shadow"></div>
  <div class="pets" role="img" aria-label="Photo of cats and dogs sitting side by side"></div>
  <div class="foot-links" style="top:1061px">Home <span>|</span> About Corvane <span>|</span> PR <span>|</span> Social Media <span>|</span> Pet Experts <span>|</span> Business Development <span>|</span> Case Studies <span>|</span> Our Team <span>|</span> Corvane Life</div>
  <div class="foot-links" style="top:1076px">Connect With Us <span>|</span> Our Blog <span>|</span> Corporate Site <span>|</span> Contact <span>|</span> Careers <span>|</span> Love List <span>|</span> Blog</div>
  <div class="foot-note">&copy;2014 The Corvane Agency | 48 Alder Crest Rd. NV 89000 | 555.014.2270</div>
  <div class="social"><i></i><i></i><i></i></div>
</footer>
</body>
</html>
```